Resume for higher management position in a mechanical/consultant industries application*

I would like to use this resume for getting a higher position interview possibilities. My skills are multi-cultural negotiation, mechanical industry sales, outsourcing to Asia, ability to manage the agent/reseller system, well team player. multi-language Chinese/English/German specialized. Please make the design, professional, comfortable to read atmosphere.

Target Market(s)

management position, sales related

Font styles to use
Serif
Sans Serif

```html
<!DOCTYPE html>
<html lang="en">
<head>
<meta charset="utf-8">
<title>Wei-Lin Hsu – Resume</title>
<link rel="stylesheet" href="https://fonts.googleapis.com/css2?family=Arimo:wght@400;500&family=Open+Sans:wght@400;500&display=swap">
<style>
  :root {
    --paper: #e6e5ea;
    --band: #262628;
    --ink: #29292b;
    --muted: #8a8a8e;
    --bar-fill: #8e8f93;
    --bar-track: #c9c9cc;
    --rule-light: #8e8e92;
  }
  * { margin: 0; padding: 0; box-sizing: border-box; }
  html, body { width: 862px; height: 1200px; overflow: hidden; }
  body { background: var(--paper); font-family: "Arimo", Arial, sans-serif; color: var(--ink); }
  .resume { position: relative; width: 862px; height: 1200px; background: var(--paper); }
  .band { position: absolute; left: 0; width: 862px; background: var(--band); }
  .band--top { top: 0; height: 36px; }
  .band--bottom { top: 1166px; height: 34px; }

  .name {
    position: absolute; top: 86px; left: 0; width: 848px; text-align: center;
    font-family: "Arimo", Arial, sans-serif; font-weight: 400; font-size: 34px;
    letter-spacing: 9px; color: var(--ink);
  }

  .section-title {
    position: absolute; font-family: "Open Sans", Arial, sans-serif; font-weight: 400;
    font-size: 16px; letter-spacing: 3.5px; line-height: 1;
  }
  .section-title--side { color: var(--muted); }
  .rule { position: absolute; height: 2px; background: var(--ink); }
  .rule--side { background: var(--rule-light); }

  .about {
    position: absolute; left: 77px; top: 253px; width: 152px;
    font-family: "Open Sans", Arial, sans-serif; font-size: 11px; line-height: 18.5px; color: var(--muted);
  }
  .contact { position: absolute; left: 77px; width: 148px; height: 38px; }
  .contact svg { position: absolute; left: 0; top: 0; }
  .contact span {
    position: absolute; right: 0; top: 10px; max-width: 104px; text-align: right;
    font-family: "Open Sans", Arial, sans-serif;
    font-size: 10.5px; color: var(--muted); white-space: nowrap;
  }

  .skill-label {
    position: absolute; left: 75px; font-family: "Open Sans", Arial, sans-serif;
    font-size: 10px; letter-spacing: 1.3px; color: var(--muted);
  }
  .skill-bar { position: absolute; left: 75px; width: 133px; height: 10px; background: var(--bar-track); }
  .skill-bar i { display: block; height: 100%; background: var(--bar-fill); }

  .job { position: absolute; left: 283px; width: 523px; }
  .job-company { font-size: 17.5px; font-weight: 400; line-height: 22px; letter-spacing: 1px; }
  .job-role { font-size: 15px; line-height: 24px; letter-spacing: 0.7px; margin-bottom: 2px; }
  .job-desc { font-size: 14px; line-height: 19.5px; text-align: justify; letter-spacing: 0.6px; }

  .edu { position: absolute; left: 281px; width: 526px; display: flex; justify-content: space-between; align-items: baseline; }
  .edu-school { font-size: 13.5px; }
  .edu-degree { font-size: 10.5px; }

  .achievements {
    position: absolute; left: 76px; top: 908px; width: 731px;
    font-size: 14.5px; line-height: 22.3px; text-align: justify; letter-spacing: 0.6px;
  }
</style>
</head>
<body>
<main class="resume">
  <div class="band band--top"></div>

  <h1 class="name">Wei-Lin Hsu</h1>

  <h2 class="section-title section-title--side" style="left:78px;top:204px;">ABOUT ME</h2>
  <div class="rule rule--side" style="left:76px;top:228px;width:145px;"></div>
  <p class="about">Coordinate Well With Team<br>To Ensure Maximum Effective-ness of Each Task.<br>Well-Versed and a history of successful Career.</p>

  <div class="contact" style="top:351px;">
    <svg width="38" height="38" viewBox="0 0 38 38" aria-hidden="true">
      <circle cx="19" cy="19" r="17.5" fill="none" stroke="var(--muted)" stroke-width="1.5"/>
      <circle cx="19" cy="14" r="5" fill="var(--muted)"/>
      <path d="M9 29c0-6 4-9 10-9s10 3 10 9z" fill="var(--muted)"/>
    </svg>
    <span>Wei-Lin Hsu</span>
  </div>
  <div class="contact" style="top:394px;">
    <svg width="38" height="38" viewBox="0 0 38 38" aria-hidden="true">
      <circle cx="19" cy="19" r="17.5" fill="none" stroke="var(--muted)" stroke-width="1.5"/>
      <rect x="13" y="9" width="12" height="20" rx="2" fill="none" stroke="var(--muted)" stroke-width="1.5"/>
      <circle cx="19" cy="26" r="1" fill="var(--muted)"/>
    </svg>
    <span>+49 170 555 0142</span>
  </div>
  <div class="contact" style="top:437px;">
    <svg width="38" height="38" viewBox="0 0 38 38" aria-hidden="true">
      <circle cx="19" cy="19" r="17.5" fill="none" stroke="var(--muted)" stroke-width="1.5"/>
      <rect x="9" y="12" width="20" height="14" fill="var(--muted)"/>
      <path d="M9 12l10 8 10-8" fill="none" stroke="var(--paper)" stroke-width="1.2"/>
    </svg>
    <span>wl.hsu@mail.example</span>
  </div>
  <div class="contact" style="top:480px;">
    <svg width="38" height="38" viewBox="0 0 38 38" aria-hidden="true">
      <circle cx="19" cy="19" r="17.5" fill="none" stroke="var(--muted)" stroke-width="1.5"/>
      <path d="M19 30c-5-6-7-10-7-13a7 7 0 0 1 14 0c0 3-2 7-7 13z" fill="var(--muted)"/>
      <circle cx="19" cy="17" r="2.6" fill="var(--paper)"/>
    </svg>
    <span>Neustadt, Germany</span>
  </div>

  <h2 class="section-title section-title--side" style="left:78px;top:527px;">SKILLS</h2>
  <div class="rule rule--side" style="left:76px;top:551px;width:145px;"></div>

  <div class="skill-label" style="top:578px;">Project Management</div>
  <div class="skill-bar" style="top:600px;"><i style="width:90%"></i></div>
  <div class="skill-label" style="top:635px;">Team Work</div>
  <div class="skill-bar" style="top:657px;"><i style="width:81%"></i></div>
  <div class="skill-label" style="top:692px;">LeaderShip Skills</div>
  <div class="skill-bar" style="top:714px;"><i style="width:95%"></i></div>
  <div class="skill-label" style="top:749px;">Public Speaking</div>
  <div class="skill-bar" style="top:771px;"><i style="width:81%"></i></div>
  <div class="skill-label" style="top:799px;">Detail-Oriented</div>
  <div class="skill-bar" style="top:821px;"><i style="width:69%"></i></div>

  <h2 class="section-title" style="left:284px;top:204px;">WORK EXPERIENCE</h2>
  <div class="rule" style="left:281px;top:228px;width:526px;"></div>

  <section class="job" style="top:253px;">
    <h3 class="job-company">ASIAXXXXXXXXX</h3>
    <p class="job-role">SALES MANAGER&nbsp; 2018 - Now</p>
    <p class="job-desc">Currently, leading 3 major dealers in Taiwan, Mainland China, South Korea and Japan with more than 20 salesmen team. Veltmann provides rotary tables, trunnions and 2 axis rotary tilt units shall have the best possible technical characteristics in the smallest possible space, is the principle model for our dividing heads -engineering -manufacturing -and assembly.</p>
  </section>

  <section class="job" style="top:409px;">
    <h3 class="job-company">KESTREL PRECISION MACHINERY COMPANY</h3>
    <p class="job-role">DIRECTOR OF MANUFACTURING, 2012-2017</p>
    <p class="job-desc">Using CNC turn/mill machine to manufacture any mechanical components as customers want. Also providing great total solutions for our clients. Photos shown in my online portfolio are my products which are made by CNC turn-milling dual spindles machines(trophy is programmed by CAM).</p>
  </section>

  <section class="job" style="top:547px;">
    <h3 class="job-company">NORTHGATE IMPORT MANNHEIM GERMANY</h3>
    <p class="job-role">MARKETING ANALYST, 2012</p>
    <p class="job-desc">Help Northgate Import to build their sales/marketing strategy for the new launched product “Slick-Mend” in central Europe.</p>
  </section>

  <section class="job" style="top:647px;">
    <h3 class="job-company">CALCESTRA GROUP BERGAMO ITALY</h3>
    <p class="job-role">EXTERNAL CONSULTANT, 2011-2012</p>
    <p class="job-desc" style="line-height:22px;">To improve the Ardent solution(ERP system) of Calcestra with re-organized procurement process and new standardized KPIs.</p>
  </section>

  <h2 class="section-title" style="left:284px;top:764px;">EDUCATION</h2>
  <div class="rule" style="left:281px;top:789px;width:529px;"></div>
  <div class="edu" style="top:814px;">
    <span class="edu-school">POLITECNICO LOMBARDO ITALY</span>
    <span class="edu-degree">MASTER OF BUSINESS ADMNISTRATION (MBA)</span>
  </div>
  <div class="edu" style="top:847px;">
    <span class="edu-school">JADE RIVER CHRISTIAN UNIVERSITY</span>
    <span class="edu-degree">BACHELOR OF CHEMICAL ENGINEERING</span>
  </div>

  <h2 class="section-title" style="left:78px;top:869px;">ACHIEVEMENTS</h2>
  <div class="rule" style="left:76px;top:894px;width:731px;"></div>
  <div class="achievements">
    <p>Mandarin Chinese/ German/ English speaker, real machining experiences, OEM skills, trade skill, global sourcing.Currently, I am a “Sales manager Asia” of a top German rotary table company. I am in charge of four countries Japan, China, South Korea and Taiwan with 3 agents, more than 20 salemen team.</p>
    <p>As a director of manufacuturing, I have more than 5 years professional experiences in manufacturing metal components by different CNC-machines. I am capable of coding CNC G,M-code, designing the wor-king path of different parts and managing the whole process.</p>
    <p>I have well-understanding of mechanical outsourcing ecosystem in Taiwan. With deep knowledge of outsourcing metal components to different suppliers in Taiwan.Familiar with coordinating with different industrial processes in order to build the final products. (Black oxidizing, Different anodizing, Chemical polishing, Manganese phosphate coating, Heat treatment, and Different grinding methods) Especially love to build prototype in order to get a high profitable potential products. (from zero to one)</p>
  </div>

  <div class="band band--bottom"></div>
</main>
</body>
</html>
```